Vorsen Kinetics Iron Tide Multi Vitamin Label Design

We need a label design for our Sports Performance Daily Multi Vitamin specially created and branded for our Vorsen Kinetics line for the Halbrook State University. The feel is edgy, sports nutrition. Two logos need to be incorporated... Vorsen and the Collective Logo attached. The colors should be the official colors of the Halbrook State University. The font may also be the Georgia font... or the Vorsen font. Or any font. A hydration product will also be created later on...so this label design may be used on many products. Please utilize the collective logo similar to the use in the attached photo. No official trademark items from the Halbrook State University should be used. Attached is also an image if the bottle (white) that will be used for the vitamin. Please use red, black, grey, white. We are looking for the front design only right now and once selected, will work on the nutrition/back label portion with the artist.

```html
<!DOCTYPE html>
<html lang="en">
<head>
<meta charset="utf-8">
<title>Vorsen Kinetics Iron Tide Multi Vitamin – Front Label</title>
<link rel="stylesheet" href="https://fonts.googleapis.com/css2?family=Alfa+Slab+One&display=swap">
<style>
  :root {
    --backdrop: #e3e3e3;
    --label-white: #ffffff;
    --label-grey: #bdbdbd;
    --brand-red: #d2394c;
    --deep-red: #b3273a;
    --ink: #1f1f1f;
  }
  * { margin: 0; padding: 0; box-sizing: border-box; }
  html, body {
    width: 1200px;
    height: 1185px;
    overflow: hidden;
    background: var(--backdrop);
  }
  .canvas {
    position: relative;
    width: 1200px;
    height: 1185px;
  }
  .label {
    position: absolute;
    left: 250px;
    top: 150px;
    width: 700px;
    height: 885px;
    box-shadow: 0 6px 24px rgba(0,0,0,0.12);
    font-family: "Alfa Slab One", Georgia, serif;
  }
  .label-shapes {
    position: absolute;
    inset: 0;
    display: block;
  }
  .brand-name {
    position: absolute;
    top: 110px;
    left: 0;
    width: 100%;
    text-align: center;
    font-size: 128px;
    line-height: 1;
    color: var(--brand-red);
    letter-spacing: 2px;
  }
  .product-title {
    position: absolute;
    left: 72px;
    top: 395px;
    font-size: 96px;
    line-height: 1.02;
    letter-spacing: 1px;
    color: var(--label-white);
  }
  .product-title .accent { color: var(--brand-red); display: block; }
  .product-title .line { display: block; }
  .collective-name {
    position: absolute;
    left: 0;
    width: 100%;
    top: 790px;
    text-align: center;
    font-size: 34px;
    letter-spacing: 2px;
    color: var(--ink);
  }
</style>
</head>
<body>
<main class="canvas">
  <section class="label" aria-label="Daily Multi Vitamin front label">
    <svg class="label-shapes" viewBox="0 0 700 885" width="700" height="885" aria-hidden="true">
      <rect class="label-base" x="0" y="0" width="700" height="885" fill="var(--label-white)"/>
      <!-- top band -->
      <path class="top-band" d="M0 0 H700 V40 C560 20 420 22 300 24 C180 26 80 22 0 30 Z" fill="var(--brand-red)"/>
      <!-- grey panel framed by red swooshes -->
      <path class="grey-panel" d="M0 330 C200 340 480 290 700 230 V760 C500 740 250 735 0 748 Z" fill="var(--label-grey)"/>
      <path class="upper-swoosh" d="M0 312 C200 322 480 272 700 212 V240 C480 300 200 350 0 340 Z" fill="var(--brand-red)"/>
      <path class="lower-swoosh" d="M0 742 C250 728 500 734 700 756 V782 C500 762 250 756 0 770 Z" fill="var(--brand-red)"/>
      <!-- bottom band -->
      <rect class="bottom-band" x="0" y="858" width="700" height="27" fill="var(--brand-red)"/>
      <rect class="bottom-band-shade" x="0" y="878" width="700" height="7" fill="var(--deep-red)"/>
    </svg>

    <h1 class="brand-name">Vorsen</h1>

    <h2 class="product-title">
      <span class="line">DAILY</span>
      <span class="line">MULTI</span>
      <span class="accent">VITAMIN</span>
    </h2>

    <p class="collective-name">NORTHGATE COLLECTIVE</p>
  </section>
</main>
</body>
</html>
```